Velmor PashuのRTZの電子書籍表紙デザインをお願いします。

*週末ごとに和みを探す読者へ贈る癒やしの四季手帳*というタイトルの表紙デザインの発注です。
サブタイトル 猫の昼寝は街を照らす
猫の昼寝は毎日を照らす
私は猫の昼寝に癒された
になります。
お笑い要素の多い1日1笑いみたいな本の表紙です。

初めての表紙デザイン依頼なので、よく勝手がわかっていませんので、
出来上がったデザインを作家グループの中で投票にかけて、
一番投票得票数の多かったものを表紙デザインとして選ばせていただきたいと考えております。
もしかしたら、その中で、何か修正依頼など来るかもしれませんが、
それも含めて、ご対応していただける方よろしくお願いします。

1部内容の抜粋を記載します。

その他何かご不明な点がございましたら、お気軽にご質問下さい。
よろしくお願いいたします。
すいません。作家名は後でお伝えします。作家名もどこかに挿入いただきたいです。よろしくお願いします。
データサイズですが、推奨サイズでJPEGファイルでご納品下さい、よろしくお願いします。
皆様、たくさんのご応募まことにありがとうございました。
現在、作家グループへ全体回覧のメールを致しました。
皆様の投票結果までお待ちください。
また、この度、いろいろな作品に触れさせていただきましたこと本当に
本当に感謝いたします。
今回の表紙に関しましては、どうしても1名しか選べない状況がございますこと
また、選挙による投票にて決定致しますこと、ご理解何卒よろしくお願い申しあげます。
また、もしも、今回当選に至らないことがありましても、
今後も私自身は作家生活を継続予定ですので、
(今回は作品の表紙に合わないことがあっても)作風の気に入ったデザイナー様には
個人的にお話を相談させていただく場合もあると思っております。
その際には何卒よろしくお願い申し上げます。この度はまことにありがとうございました。
この度はご応募まことにありがとうございました。厳選なる選挙の結果、1名の作家さんが選ばれました。
選ばれました方には個別にお伝えいたしております。この度はまことにご応募ありがとうございました。

作家メンバーによる総選挙にて決定させて頂きました。皆様に広く愛される作品で、投票数も多く選ばせて頂きました。誠にありがとうございました。

今回、誠にご提案ありがとうございました。私自身は作家活動を継続していくつもりですので、また、個別にご依頼させて頂くこともあるかと思います。その時はよろしくお願いします。この度はありがとうございました。

```html
<!DOCTYPE html>
<html lang="ja">
<head>
<meta charset="UTF-8">
<title>週末ごとに和みを探す読者へ贈る癒やしの四季手帳</title>
<link rel="stylesheet" href="https://fonts.googleapis.com/css2?family=M+PLUS+Rounded+1c:wght@500;700;800&display=swap">
<style>
  :root {
    --paper: #ffffff;
    --ink: #333333;
    --ink-soft: #666666;
    --accent: #f15a24;
    --band: #f0592a;
    --sun: #f6c21d;
    --art-top: #fdf3d8;
    --art-bottom: #fbe2c4;
  }
  * { margin: 0; padding: 0; box-sizing: border-box; }
  html, body { width: 750px; height: 1200px; overflow: hidden; background: var(--paper); }
  body { font-family: "M PLUS Rounded 1c", sans-serif; color: var(--ink); }
  .cover { position: relative; width: 750px; height: 1200px; background: var(--paper); overflow: hidden; }

  .kicker {
    position: absolute; top: 38px; left: 0; width: 750px;
    text-align: center; font-weight: 800; font-size: 44px; color: var(--ink);
  }
  .kicker-rays { position: absolute; top: 20px; left: 225px; width: 300px; height: 80px; }

  .lead {
    position: absolute; top: 112px; left: 0; width: 750px;
    text-align: center; font-weight: 800; font-size: 54px; color: var(--accent); letter-spacing: 1px;
  }

  .badge {
    position: absolute; top: 222px; left: 92px; width: 160px; height: 160px;
  }
  .badge-text {
    position: absolute; top: 276px; left: 92px; width: 160px;
    text-align: center; font-weight: 800; font-size: 40px; color: var(--paper);
  }

  .main-title {
    position: absolute; top: 218px; left: 272px;
    font-weight: 800; font-size: 88px; line-height: 94px; color: var(--ink); letter-spacing: 4px;
  }

  .author {
    position: absolute; top: 472px; left: 0; width: 750px;
    text-align: center; font-weight: 500; font-size: 30px; color: var(--ink-soft); letter-spacing: 2px;
  }

  .art {
    position: absolute; top: 530px; left: 40px; width: 670px; height: 430px;
    background: linear-gradient(180deg, var(--art-top), var(--art-bottom));
    border-radius: 24px;
  }

  .tagline-band {
    position: absolute; top: 935px; left: 0; width: 750px; height: 265px;
    background: var(--band);
    display: flex; flex-direction: column; justify-content: center; align-items: center;
  }
  .tagline {
    font-weight: 800; font-size: 58px; line-height: 78px; color: var(--paper); white-space: nowrap;
  }
</style>
</head>
<body>
<main class="cover">
  <svg class="kicker-rays" viewBox="0 0 300 80" aria-hidden="true">
    <g stroke="#f6c21d" stroke-width="6" stroke-linecap="round">
      <line x1="28" y1="20" x2="42" y2="36"/>
      <line x1="14" y1="48" x2="34" y2="52"/>
      <line x1="272" y1="20" x2="258" y2="36"/>
      <line x1="286" y1="48" x2="266" y2="52"/>
    </g>
  </svg>
  <p class="kicker">週末ごとに</p>
  <p class="lead">和みを探す読者へ贈る</p>

  <svg class="badge" viewBox="0 0 160 160" aria-hidden="true">
    <circle cx="80" cy="80" r="76" fill="#f15a24"/>
  </svg>
  <p class="badge-text">癒やしの</p>

  <h1 class="main-title">四季<br>手帳</h1>

  <p class="author">著者氏名</p>

  <div class="art" role="img" aria-label="両手を上げて楽しそうに跳ねる子どもたちのイラスト"></div>

  <section class="tagline-band">
    <p class="tagline">猫の昼寝は街を照らす</p>
    <p class="tagline">猫の昼寝は毎日を照らす</p>
    <p class="tagline">私は猫の昼寝に癒された</p>
  </section>
</main>
</body>
</html>
```